Folded A4 flyer for design&construction company

Folded A4 flyer needed. Keywords: elegant, stylish
our website www.dravimo.ae

Industry/Entity Type

Construction

```html
<!DOCTYPE html>
<html lang="en">
<head>
<meta charset="utf-8">
<title>Dravimo – Folded A4 Flyer</title>
<link href="https://fonts.googleapis.com/css2?family=EB+Garamond:ital,wght@0,400;0,500;1,400&family=Open+Sans:ital,wght@0,400;0,600;1,400&family=Parisienne&display=swap" rel="stylesheet">
<style>
  :root {
    --gold: #d4ad2a;
    --gold-light: #f0d257;
    --gold-deep: #b88f17;
    --cream: #fdfbf3;
    --ink: #1d1d1b;
    --text: #3a3a36;
    --bg: #ffffff;
  }
  * { box-sizing: border-box; margin: 0; padding: 0; }
  html, body { width: 1200px; height: 1200px; overflow: hidden; background: var(--bg); }
  body { position: relative; font-family: "EB Garamond", serif; color: var(--text); }

  .spread { position: absolute; display: flex; box-shadow: 0 6px 24px rgba(0,0,0,.12); }
  .spread--outer { left: 60px; top: 40px; }
  .spread--inner { left: 420px; top: 630px; }

  .page {
    position: relative; width: 382px; height: 540px;
    background: linear-gradient(135deg, var(--gold-light), var(--gold) 55%, var(--gold-deep));
    padding: 10px;
  }
  .page + .page { border-left: 1px solid rgba(0,0,0,.08); }
  .page__inner { position: relative; width: 100%; height: 100%; background: var(--cream); overflow: hidden; }

  .flourish {
    position: absolute; width: 52px; height: 52px;
    background: radial-gradient(circle at 35% 35%, var(--gold-light), var(--gold) 55%, transparent 72%);
    opacity: .8;
  }
  .flourish--tl { top: 0; left: 0; border-radius: 0 0 60% 0; }
  .flourish--tr { top: 0; right: 0; border-radius: 0 0 0 60%; }
  .flourish--bl { bottom: 0; left: 0; border-radius: 0 60% 0 0; }
  .flourish--br { bottom: 0; right: 0; border-radius: 60% 0 0 0; }
  .flourish--top { top: 0; left: 50%; width: 150px; height: 80px; margin-left: -75px; border-radius: 0 0 75px 75px; }

  .wordmark { font-family: "Open Sans", sans-serif; font-weight: 400; color: var(--ink); letter-spacing: .5px; line-height: 1; }

  /* back page */
  .back { text-align: center; }
  .back .wordmark { font-size: 24px; margin-top: 100px; }
  .back__about { font-size: 9.5px; line-height: 1.35; margin: 16px 44px 0; color: var(--ink); }
  .back__cta { margin-top: 56px; font-size: 17px; line-height: 1.25; letter-spacing: .5px; color: var(--ink); }
  .back__rule { width: 124px; height: 1px; background: var(--text); margin: 10px auto 8px; opacity: .6; }
  .back__contact { font-size: 11px; line-height: 1.4; letter-spacing: .4px; color: var(--ink); }
  .back__footer {
    position: absolute; left: 0; right: 0; bottom: 0; height: 62px;
    background: linear-gradient(90deg, var(--gold-deep), var(--gold-light) 50%, var(--gold));
    display: flex; flex-direction: column; justify-content: center; align-items: center; color: var(--ink);
  }
  .back__web { font-style: italic; font-size: 12px; }
  .back__address { font-size: 8.5px; }

  /* front page */
  .front .wordmark { position: absolute; top: 170px; left: 0; right: 0; text-align: center; font-size: 66px; font-weight: 600; }
  .front__band {
    position: absolute; left: 0; right: 0; top: 356px; height: 56px;
    background: linear-gradient(90deg, var(--gold-deep), var(--gold-light) 50%, var(--gold));
  }
  .front__quote { position: absolute; left: 106px; top: 334px; width: 150px; height: 100px; }
  .front__quote-text {
    position: absolute; inset: 0; display: flex; flex-direction: column; justify-content: center; align-items: center;
    font-family: "Open Sans", sans-serif; color: var(--ink); text-align: center;
  }
  .front__quote-line { font-style: italic; font-size: 10.5px; line-height: 1.3; }
  .front__quote-author { font-size: 7.5px; margin-top: 4px; padding-top: 3px; border-top: 1px solid var(--ink); }

  /* inner pages */
  .service { position: absolute; left: 64px; }
  .service__head { display: flex; align-items: baseline; gap: 12px; white-space: nowrap; }
  .service__title { font-family: "Parisienne", cursive; font-size: 25px; font-weight: 400; color: var(--ink); }
  .service__head .wordmark { font-size: 13px; }
  .service__list { list-style: none; margin-top: 8px; }
  .service__list li { font-size: 10.5px; line-height: 18.5px; padding-left: 16px; position: relative; color: var(--ink); white-space: nowrap; }
  .service__list li::before {
    content: ""; position: absolute; left: 2px; top: 7px; width: 5px; height: 5px;
    background: var(--gold); transform: rotate(45deg);
  }
  .photo { position: absolute; border: 4px solid #fff; box-shadow: 0 2px 6px rgba(0,0,0,.25); }
  .photo--interior { right: 16px; top: 70px; width: 126px; height: 92px; transform: rotate(-6deg); background: linear-gradient(135deg, #e9d7a7, #b58b52 60%, #7a5a3a); }
  .photo--garden { right: 12px; top: 364px; width: 104px; height: 72px; transform: rotate(-2deg); background: linear-gradient(180deg, #c7dbe8, #7fa04d 45%, #b56b4b); }
  .photo--fitout { right: 14px; top: 62px; width: 120px; height: 84px; transform: rotate(-2deg); background: linear-gradient(135deg, #f0f0ee, #c9a27a 60%, #5b6c86); }
  .photo--tools { right: 16px; top: 332px; width: 120px; height: 88px; transform: rotate(-5deg); background: linear-gradient(135deg, #3f5e86, #c98a3b 55%, #e9e2d2); }
</style>
</head>
<body>

<section class="spread spread--outer" aria-label="Flyer outside: back and front cover">
  <article class="page">
    <div class="page__inner back">
      <div class="flourish flourish--tl" role="img" aria-label="Gold baroque corner ornament"></div>
      <div class="flourish flourish--tr" role="img" aria-label="Gold baroque corner ornament"></div>
      <p class="wordmark">DRAVIMO</p>
      <p class="back__about">We believe in quality beginnings and flawless finishes. We are a team of creative designers and constructors with years of experience and expertise in providing complete interior design and construction services. Our unique designing prowess is complemented by our unflinching commitment to quality construction. Our team specializes in classic and contemporary high quality construction in Dubai for commercial and residential projects.</p>
      <p class="back__cta">GET A<br>FREE QUOTE<br>TODAY!</p>
      <div class="back__rule"></div>
      <p class="back__contact">800 – DRAVIMO<br>OR<br>CONTACT@DRAVIMO.AE</p>
      <footer class="back__footer">
        <p class="back__web">www.dravimo.ae</p>
        <p class="back__address">Dravimo LLC, Harbor Point Tower, Office 1304, Business Bay, Dubai</p>
      </footer>
    </div>
  </article>
  <article class="page">
    <div class="page__inner front">
      <div class="flourish flourish--top" role="img" aria-label="Gold baroque top ornament"></div>
      <h1 class="wordmark">DRAVIMO</h1>
      <div class="front__band"></div>
      <div class="front__quote">
        <svg width="150" height="100" viewBox="0 0 150 100" aria-hidden="true">
          <defs>
            <linearGradient id="plaque" x1="0" y1="0" x2="1" y2="1">
              <stop offset="0" stop-color="#f0d257"/><stop offset="1" stop-color="#c99e1f"/>
            </linearGradient>
          </defs>
          <rect x="3" y="3" width="144" height="94" rx="18" fill="url(#plaque)" stroke="#b88f17" stroke-width="2"/>
          <rect x="10" y="10" width="130" height="80" rx="13" fill="none" stroke="#8f6d0f" stroke-width="1"/>
        </svg>
        <div class="front__quote-text">
          <span class="front__quote-line">Quality is not an act,<br>it is a habit</span>
          <span class="front__quote-author">E. Marlow</span>
        </div>
      </div>
    </div>
  </article>
</section>

<section class="spread spread--inner" aria-label="Flyer inside: services">
  <article class="page">
    <div class="page__inner">
      <div class="flourish flourish--tl" role="img" aria-label="Gold baroque corner ornament"></div>
      <div class="flourish flourish--tr" role="img" aria-label="Gold baroque corner ornament"></div>
      <div class="flourish flourish--bl" role="img" aria-label="Gold baroque corner ornament"></div>
      <div class="flourish flourish--br" role="img" aria-label="Gold baroque corner ornament"></div>
      <div class="service" style="top:58px">
        <div class="service__head"><h2 class="service__title">Design</h2><span class="wordmark">DRAVIMO</span></div>
        <ul class="service__list">
          <li>Villas Interior Design</li><li>Villas Exterior Design</li><li>Landscape Design</li>
          <li>Retail Interior Design</li><li>Office Interior Design</li><li>Hospitality Interior Design</li>
          <li>Hotel Interior Design</li><li>Hotel Exterior Design</li><li>Restaurant Interior Design</li>
        </ul>
      </div>
      <div class="photo photo--interior" role="img" aria-label="Photo of a luxurious classic living room interior"></div>
      <div class="service" style="top:318px">
        <div class="service__head"><h2 class="service__title">Landscaping</h2><span class="wordmark">DRAVIMO</span></div>
        <ul class="service__list">
          <li>Soft Landscaping</li><li>Irrigation Solutions</li><li>Hard land Scaping</li>
          <li>External Lighting</li><li>Swimming Pool &amp; Water Features</li>
        </ul>
      </div>
      <div class="photo photo--garden" role="img" aria-label="Photo of a landscaped garden with lawn and paved path"></div>
    </div>
  </article>
  <article class="page">
    <div class="page__inner">
      <div class="flourish flourish--tl" role="img" aria-label="Gold baroque corner ornament"></div>
      <div class="flourish flourish--tr" role="img" aria-label="Gold baroque corner ornament"></div>
      <div class="flourish flourish--bl" role="img" aria-label="Gold baroque corner ornament"></div>
      <div class="flourish flourish--br" role="img" aria-label="Gold baroque corner ornament"></div>
      <div class="service" style="top:50px">
        <div class="service__head"><h2 class="service__title">Fitout</h2><span class="wordmark">DRAVIMO</span></div>
        <ul class="service__list">
          <li>Development Approvals</li><li>Flooring Solutions</li><li>Partition</li><li>Sealing Solutions</li>
          <li>MEP Works</li><li>Civil Works</li><li>Joinery</li><li>Glass and Aluminium Works (subcontractor)</li>
        </ul>
      </div>
      <div class="photo photo--fitout" role="img" aria-label="Photo of laminate flooring being installed with tools"></div>
      <div class="service" style="top:288px">
        <div class="service__head"><h2 class="service__title">Maintaince</h2><span class="wordmark">DRAVIMO</span></div>
        <ul class="service__list">
          <li>AC Repair</li><li>Plumber Services</li><li>Electric Repair</li><li>Carpentry Work</li>
          <li>Gypsum Ceiling</li><li>Painting Services</li><li>Cleaning Services</li><li>Emergency Services</li>
        </ul>
      </div>
      <div class="photo photo--tools" role="img" aria-label="Photo of a leather tool belt with work gloves and hand tools"></div>
    </div>
  </article>
</section>

</body>
</html>
```